Calm Harbor website development

Need a website designed for a coaching business. Very high-end, luxury, professionalism, in the area of STRESS, see brief attached. I have a logo already
Updates

Slow in providing feedback

Target Market(s)

CEOs very successful men and wealthy females, high end luxury market

Industry/Entity Type

coaching

Number of Pages Required

1 page

Requirements
Must have
• Luxury look, professional, serious but warm, appealing to both sexes

```html
<!DOCTYPE html>
<html lang="en">
<head>
<meta charset="utf-8">
<title>Calm Harbor — Lifestyle Coaching</title>
<link rel="stylesheet" href="https://fonts.googleapis.com/css2?family=Montserrat:wght@500;600;700&family=Lato:wght@400;700&display=swap">
<style>
:root{
  --blue:#14a3f5;
  --grey:#6d6e71;
  --ink:#1f1f1f;
  --text:#3a3a3a;
  --soft:#f5f6f8;
  --white:#ffffff;
}
*{box-sizing:border-box;margin:0;padding:0}
html,body{width:1200px;height:2836px;overflow:hidden;background:var(--white)}
body{position:relative;font-family:"Lato",sans-serif;color:var(--text)}
.abs{position:absolute}
.heading{font-family:"Montserrat",sans-serif;font-weight:600;color:var(--ink);text-transform:uppercase;white-space:nowrap}

/* top bar */
.topbar{left:0;top:0;width:1200px;height:36px}
.topbar-text{top:8px;font-size:15px;color:var(--white);white-space:nowrap}
.topbar-social{top:10px;display:flex;gap:14px}
.topbar-social span{width:13px;height:13px;border-radius:50%;background:var(--white);display:block}

/* header */
.brand{left:90px;top:8px;width:140px;text-align:center}
.brand-dot{width:34px;height:34px;border-radius:50%;background:var(--ink);margin:0 auto 6px}
.brand-name{font-family:"Montserrat",sans-serif;font-weight:700;font-size:12px;letter-spacing:1.2px;color:var(--ink);white-space:nowrap}
.brand-tag{font-size:6px;letter-spacing:1px;color:var(--text);margin-top:1px;white-space:nowrap}
.nav{top:54px;font-size:16px;color:#333;white-space:nowrap}
.nav-active::after{content:"";position:absolute;left:0;right:0;top:25px;height:3px;background:var(--blue)}
.phone-badge{left:916px;top:48px;width:28px;height:30px}
.phone-text{left:959px;top:55px;font-size:16px;font-weight:700;color:#222;white-space:nowrap}
.header-line{left:0;top:94px;width:1200px;height:1px;background:#e5e5e5}

/* hero */
.hero{left:0;top:94px;width:1200px;height:612px}
.hero-title{left:108px;top:272px;font-family:"Montserrat",sans-serif;font-weight:600;font-size:60px;color:var(--white);letter-spacing:1px;white-space:nowrap}
.hero-sub{left:110px;top:350px;font-size:19px;line-height:26px;color:var(--white);font-weight:400;white-space:nowrap}
.pill{display:flex;align-items:center;border-radius:24px;font-family:"Montserrat",sans-serif;font-weight:500;color:var(--white);white-space:nowrap}
.pill-dot{width:36px;height:36px;border-radius:50%;background:var(--white);border:5px solid #d9d9d9;flex:none;margin-left:4px}
.pill-label{flex:1;text-align:center;padding-right:20px}
.hero-btn{top:425px;height:44px;background:var(--blue);font-size:19px}
.slider-dot{left:1136px;width:11px;height:11px;border-radius:50%;background:var(--white)}

/* about & why */
.section-h1{font-size:31px}
.section-h2{font-size:26px}
.para{font-size:15.6px;line-height:25.7px;color:var(--text)}
.dark-btn{height:44px;background:var(--grey);font-size:16px;font-family:"Lato",sans-serif;font-weight:700}

/* benefits */
.benefits{left:0;top:1319px;width:1200px;height:704px;background:var(--soft)}
.benefits-title{left:0;top:1360px;width:1200px;text-align:center;font-size:31px}
.benefits-sub{left:0;top:1413px;width:1200px;text-align:center;font-size:16px;color:#333}
.tile{width:243px;height:242px}
.tile-grey{background:var(--grey)}
.tile-blue{background:var(--blue)}
.tile-title{font-family:"Montserrat",sans-serif;font-weight:600;font-size:22px;color:var(--white);text-transform:uppercase;position:absolute;left:20px;top:26px;white-space:nowrap}
.tile-rule{position:absolute;left:20px;top:70px;width:52px;height:3px;background:var(--white)}
.tile-copy{position:absolute;left:24px;top:94px;width:196px;font-size:15.5px;line-height:24px;color:var(--white)}
.tile-link{position:absolute;left:27px;top:198px;font-size:15.5px;font-weight:700;color:var(--white);display:flex;align-items:center;gap:8px;white-space:nowrap}

/* footer */
.footer-links{top:2707px;font-size:16px;font-weight:700;color:var(--white);white-space:nowrap}
.foot-social{top:2697px;width:34px;height:38px}
.email{left:818px;top:2695px;width:272px;height:46px;border-radius:23px;background:var(--white)}
.email-ph{position:absolute;left:20px;top:13px;font-size:15px;color:#999}
.email-btn{position:absolute;right:0;top:0;width:108px;height:46px;border-radius:23px;background:var(--blue);color:var(--white);font-family:"Montserrat",sans-serif;font-weight:600;font-size:15px;display:flex;align-items:center;justify-content:center}
.footer-rule{left:111px;top:2774px;width:978px;height:1px;background:#9a9b9e}
.copyright{left:0;top:2797px;width:1200px;text-align:center;font-size:15px;color:var(--white)}
</style>
</head>
<body>

<!-- top bar -->
<svg class="abs topbar" viewBox="0 0 1200 36" aria-hidden="true">
  <polygon points="259,0 1200,0 1200,22 1180,36 290,36" fill="var(--blue)"/>
  <line x1="771" y1="7" x2="771" y2="27" stroke="#fff" stroke-width="1"/>
  <circle cx="398" cy="17" r="7" fill="none" stroke="#fff" stroke-width="1.6"/>
  <path d="M398 13v4.5h3" fill="none" stroke="#fff" stroke-width="1.6"/>
</svg>
<div class="abs topbar-text" style="left:423px">Mon - Fri 9.00 - 17.30 Sunday CLOSED</div>
<div class="abs topbar-text" style="left:854px">Stay connected :</div>
<div class="abs topbar-social" style="left:980px"><span></span><span></span><span></span><span></span></div>

<!-- header -->
<div class="abs brand">
  <div class="brand-dot"></div>
  <div class="brand-name">CALM HARBOR</div>
  <div class="brand-tag">— LIFESTYLE COACHING —</div>
</div>
<div class="abs nav nav-active" style="left:470px">Home</div>
<div class="abs nav" style="left:547px">About</div>
<div class="abs nav" style="left:625px">Benefits</div>
<div class="abs nav" style="left:719px">Our Blog</div>
<div class="abs nav" style="left:816px">Contact</div>
<svg class="abs phone-badge" viewBox="0 0 28 30" aria-hidden="true">
  <polygon points="14,0 28,8 28,22 14,30 0,22 0,8" fill="var(--blue)"/>
  <path d="M10 9c-1 1-1 3 1 6s4 5 6 5c1 0 2-1 2-2l-2-2-2 1c-1-1-3-3-3-4l1-2-2-2z" fill="#fff"/>
</svg>
<div class="abs phone-text">+1(555) 214 7390</div>
<div class="abs header-line"></div>

<!-- hero -->
<svg class="abs hero" viewBox="0 0 1200 612" role="img" aria-label="Photo of a woman relaxing with a cup of tea by a bright window">
  <defs>
    <linearGradient id="heroGrad" x1="0" y1="0" x2="1" y2="0">
      <stop offset="0" stop-color="#8e9296"/>
      <stop offset="0.45" stop-color="#b8bcbf"/>
      <stop offset="0.7" stop-color="#d9cfc6"/>
      <stop offset="1" stop-color="#a7a9ab"/>
    </linearGradient>
  </defs>
  <polygon points="0,0 1200,0 1200,533 1090,605 110,605 0,533" fill="url(#heroGrad)"/>
  <polyline points="0,537 110,605 1090,605 1200,537" fill="none" stroke="var(--blue)" stroke-width="7"/>
</svg>
<div class="abs hero-title">HEAD COACH</div>
<div class="abs hero-sub">Ut Enim Ad Minima Veniam, Quis Nostrum<br>Exercitationem Ullam Corporis Suscipit</div>
<div class="abs pill hero-btn" style="left:111px;width:175px"><span class="pill-dot"></span><span class="pill-label">MEN</span></div>
<div class="abs pill hero-btn" style="left:300px;width:175px"><span class="pill-dot"></span><span class="pill-label">WOMEN</span></div>
<div class="abs slider-dot" style="top:340px"></div>
<div class="abs slider-dot" style="top:364px"></div>
<div class="abs slider-dot" style="top:388px"></div>

<!-- about -->
<svg class="abs" style="left:114px;top:776px" width="406" height="458" viewBox="0 0 406 458" role="img" aria-label="Photo of a woman in a yoga pose outdoors in a park">
  <defs>
    <linearGradient id="aboutGrad" x1="0" y1="0" x2="0" y2="1">
      <stop offset="0" stop-color="#cfe0ee"/>
      <stop offset="0.55" stop-color="#9bb28f"/>
      <stop offset="1" stop-color="#6f8a4e"/>
    </linearGradient>
  </defs>
  <polygon points="202,10 400,116 400,342 202,450 10,342 10,116" fill="url(#aboutGrad)"/>
  <polyline points="4,330 4,112 202,4" fill="none" stroke="var(--blue)" stroke-width="7"/>
  <polyline points="50,378 202,456 260,426" fill="none" stroke="var(--grey)" stroke-width="6"/>
</svg>
<div class="abs heading section-h1" style="left:639px;top:816px">About Us</div>
<div class="abs heading section-h2" style="left:638px;top:864px">Welcome to CalmHarbor</div>
<p class="abs para" style="left:638px;top:910px;width:440px">Calm Harbor came about due to my desire to help people lead a better and healthier life. Initially, I was involved in the fitness/body side of health. As years passed and my experience grew, I realized how important the mind was in total wellness, and that the mind is all powerful and controlling. Control the mind, control the body and achieve success. Stress can be the most debilating factor in our lives, it is the root cause of so many diseases and costs the US</p>
<div class="abs pill dark-btn" style="left:633px;top:1141px;width:193px"><span class="pill-dot"></span><span class="pill-label">LEARN MORE</span></div>

<!-- benefits -->
<div class="abs benefits"></div>
<div class="abs heading benefits-title">Our Benefits</div>
<div class="abs benefits-sub">Sector expert Health/Wellness. Presented at numerous industry shows and quoted in national publications</div>

<div class="abs tile" style="left:111px;top:1471px;background:linear-gradient(135deg,#d8bfa0,#b7977a)" role="img" aria-label="Photo of two women relaxing in a sauna"></div>
<div class="abs tile tile-grey" style="left:354px;top:1471px">
  <div class="tile-title">Wellness</div><div class="tile-rule"></div>
  <div class="tile-copy">General issues...I live near very wealthy neighborhoods with lots of “trophy wives”</div>
  <div class="tile-link">LEARN MORE <svg width="16" height="14" viewBox="0 0 16 14"><path d="M1 7h13M8 1l6 6-6 6" fill="none" stroke="#fff" stroke-width="2"/></svg></div>
</div>
<div class="abs tile" style="left:597px;top:1471px;background:linear-gradient(135deg,#e9e4dd,#c9c2b8)" role="img" aria-label="Photo of a woman meditating at home"></div>
<div class="abs tile tile-blue" style="left:840px;top:1471px;width:244px">
  <div class="tile-title">Yoga</div><div class="tile-rule"></div>
  <div class="tile-copy">voluptatem sequi nesciunt. Neque porro quisquam est, qui dolorem ipsum quia</div>
  <div class="tile-link">LEARN MORE <svg width="16" height="14" viewBox="0 0 16 14"><path d="M1 7h13M8 1l6 6-6 6" fill="none" stroke="#fff" stroke-width="2"/></svg></div>
</div>
<div class="abs tile tile-grey" style="left:111px;top:1713px">
  <div class="tile-title" style="left:26px">Aromatherapy</div><div class="tile-rule" style="left:30px"></div>
  <div class="tile-copy" style="left:30px;width:180px">magni dolores eos qui ratione voluptatem sequi nesciunt. Neque porro</div>
  <div class="tile-link" style="left:34px">LEARN MORE <svg width="16" height="14" viewBox="0 0 16 14"><path d="M1 7h13M8 1l6 6-6 6" fill="none" stroke="#fff" stroke-width="2"/></svg></div>
</div>
<div class="abs tile" style="left:354px;top:1713px;background:linear-gradient(135deg,#c99a7c,#efe3da)" role="img" aria-label="Photo of a woman receiving a relaxing massage"></div>
<div class="abs tile tile-grey" style="left:597px;top:1713px">
  <div class="tile-title" style="left:26px">Vinyasa Yoga</div><div class="tile-rule" style="left:30px"></div>
  <div class="tile-copy" style="left:30px;width:190px">Aute Irure Dolor In Reprehenderit In Voluptate Velit Esse Cillum Dolore Eu</div>
  <div class="tile-link" style="left:33px">LEARN MORE <svg width="16" height="14" viewBox="0 0 16 14"><path d="M1 7h13M8 1l6 6-6 6" fill="none" stroke="#fff" stroke-width="2"/></svg></div>
</div>
<div class="abs tile" style="left:840px;top:1713px;width:244px;background:linear-gradient(135deg,#b7765f,#d9c2b5)" role="img" aria-label="Photo of a yoga class sitting cross-legged in a brick studio"></div>

<!-- why me -->
<div class="abs heading section-h1" style="left:111px;top:2108px">Why Me</div>
<div class="abs heading section-h2" style="left:111px;top:2157px">Vel Illum Qui Dolorem Eum</div>
<p class="abs para" style="left:111px;top:2201px;width:450px">Duis Aute Irure Dolor In Reprehenderit In Voluptate Velit Esse Cillum Dolore Eu Fugiat Nulla Pariatur. Excepteur Sint Occaecat Cupidatat Non Proident, Sunt In Culpa Qui Officia Deserunt Mollit Anim Id Est Laborum Sed ut perspiciatis unde omnis iste natus error sit voluptatem accusantium doloremque laudantium, totam rem aperiam, eaque ipsa quae ab illo inventore veritatis et quasi architecto beatae vitae dicta sunt explicabo. Nemo enim ipsam voluptatem quia</p>
<div class="abs pill dark-btn" style="left:106px;top:2433px;width:194px"><span class="pill-dot"></span><span class="pill-label">LEARN MORE</span></div>

<svg class="abs" style="left:664px;top:2078px" width="428" height="478" viewBox="0 0 428 478" role="img" aria-label="Photo of a woman meditating cross-legged in a bright room">
  <defs>
    <linearGradient id="whyGrad" x1="0" y1="0" x2="0" y2="1">
      <stop offset="0" stop-color="#e8e2dc"/>
      <stop offset="0.6" stop-color="#d4d0cc"/>
      <stop offset="1" stop-color="#4a4a4e"/>
    </linearGradient>
  </defs>
  <polygon points="212,10 414,126 414,356 212,472 12,356 12,126" fill="url(#whyGrad)"/>
  <polyline points="220,4 420,118 420,352" fill="none" stroke="var(--blue)" stroke-width="7"/>
  <polyline points="6,130 6,360 212,476" fill="none" stroke="var(--grey)" stroke-width="6"/>
</svg>

<!-- footer -->
<svg class="abs" style="left:0;top:2612px" width="1200" height="224" viewBox="0 0 1200 224" aria-hidden="true">
  <polygon points="0,86 110,16 1084,16 1200,86 1200,224 0,224" fill="var(--grey)"/>
  <polyline points="0,74 110,8 1084,8 1200,74" fill="none" stroke="var(--blue)" stroke-width="7"/>
</svg>
<svg class="abs foot-social" style="left:111px" viewBox="0 0 34 38" aria-hidden="true"><polygon points="17,0 34,9 34,29 17,38 0,29 0,9" fill="#fff"/><circle cx="17" cy="19" r="5" fill="var(--blue)"/></svg>
<svg class="abs foot-social" style="left:154px" viewBox="0 0 34 38" aria-hidden="true"><polygon points="17,0 34,9 34,29 17,38 0,29 0,9" fill="#fff"/><circle cx="17" cy="19" r="5" fill="var(--blue)"/></svg>
<svg class="abs foot-social" style="left:196px" viewBox="0 0 34 38" aria-hidden="true"><polygon points="17,0 34,9 34,29 17,38 0,29 0,9" fill="#fff"/><circle cx="17" cy="19" r="5" fill="var(--blue)"/></svg>
<svg class="abs foot-social" style="left:239px" viewBox="0 0 34 38" aria-hidden="true"><polygon points="17,0 34,9 34,29 17,38 0,29 0,9" fill="#fff"/><circle cx="17" cy="19" r="5" fill="var(--blue)"/></svg>

<div class="abs footer-links" style="left:416px">Home</div>
<div class="abs footer-links" style="left:480px">About</div>
<div class="abs footer-links" style="left:548px">Benefits</div>
<div class="abs footer-links" style="left:628px">Our Blog</div>
<div class="abs footer-links" style="left:711px">Contact</div>

<div class="abs email">
  <span class="email-ph">Your Email</span>
  <span class="email-btn">SUBMIT</span>
</div>
<div class="abs footer-rule"></div>
<div class="abs copyright">Copyright © 2022. Lumen Studio All rights reservedv</div>

</body>
</html>
```